Animal Facility Brochure for Pet Boarding, Boutique, Doggie Daycare, Grooming

This brochure is for a Doggie Daycare, Pet Grooming, Dog Boarding & Pet Boutique for the Hollowmere Pet Lodge & Spa.

Hi there! I am in need of a brochure done for my new up and coming business.
The business will involve Dog/Cat Grooming, Dog Boarding, Doggie Daycare, & a small pet boutique. I am looking for something that stands out and is modern and chic and follows the look of the pictures i have posted (Pim and Tessel) . My color scheme of my business is gray & white. Also i need the brochure to be easily able to understand what we are trying to get across and is easy to read. I am very proud of my logo that was created using craft hive and would love that incorporated. also i have attached the information that will need to be in the brochure for the client. I am looking for someone who can devote some time working with me on this because this is my first time. I am sure there will need to be some changes so i need someone who is patient. The picture of the projected look of my sign is gearing more towards something clean and modern.

Industry/Entity Type

Pet Care

Colors
f5f5f5
f8f8f8
dbdbdb
959595
aaaaaa
85abd2
cedeed
eaf1f7

Requirements
Nice to have
• File nine for Grooming, Boarding, Daycare, Pet Boutique

```html
<!DOCTYPE html>
<html lang="en">
<head>
<meta charset="utf-8">
<title>Hollowmere Pet Lodge &amp; Spa – Trifold Brochure</title>
<link rel="stylesheet" href="https://fonts.googleapis.com/css2?family=Cinzel:wght@400;600&family=Trocchi&family=Montserrat:wght@400;500;600&display=swap">
<style>
  :root {
    --ink: #2e2e2e;
    --ink-soft: #4a4a4a;
    --paper: #f8f8f8;
    --rule: #aaaaaa;
    --line: #dbdbdb;
    --stage: #cfcfcf;
  }
  * { box-sizing: border-box; margin: 0; padding: 0; }
  html, body { width: 1080px; height: 1200px; overflow: hidden; }
  body {
    background: var(--stage);
    font-family: "Montserrat", sans-serif;
    color: var(--ink);
    position: relative;
  }

  .sheet {
    position: absolute;
    left: 40px;
    width: 1000px;
    height: 570px;
    background: var(--paper);
    box-shadow: 0 2px 8px rgba(0,0,0,.18);
    overflow: hidden;
  }
  .sheet--outside { top: 15px; }
  .sheet--inside { top: 615px; }
  .fold {
    position: absolute; top: 0; bottom: 0; width: 1px;
    background: linear-gradient(var(--line), #e9e9e9, var(--line));
  }
  .fold--a { left: 333px; }
  .fold--b { left: 666px; }
  .swoosh { position: absolute; inset: 0; width: 1000px; height: 570px; }

  .panel { position: absolute; top: 0; width: 333px; height: 570px; }
  .panel--1 { left: 0; }
  .panel--2 { left: 333px; }
  .panel--3 { left: 666px; }
  .block { position: absolute; left: 28px; right: 28px; }

  .heading {
    font-family: "Cinzel", serif;
    font-weight: 600;
    font-size: 14px;
    line-height: 1.3;
    letter-spacing: .4px;
    color: var(--ink);
  }
  .center { text-align: center; }
  .body-text { font-size: 9.5px; line-height: 1.38; color: var(--ink-soft); }
  .body-text--tight { font-size: 9px; line-height: 1.32; }
  .justify { text-align: justify; }
  .flourish { display: block; margin: 5px auto 8px; width: 60px; height: 1px; background: var(--rule); }

  .wordmark { text-align: center; }
  .wordmark__dot {
    width: 20px; height: 20px; border-radius: 50%;
    background: var(--ink); margin: 0 auto 8px;
  }
  .wordmark__name {
    font-family: "Cinzel", serif; font-weight: 600;
    font-size: 18px; line-height: 1.2; color: var(--ink);
  }
  .wordmark--large .wordmark__name { font-size: 23px; }

  .hours { width: 100%; font-size: 11px; border-collapse: collapse; }
  .hours td { padding: 2px 0; color: var(--ink-soft); }
  .hours td:last-child { text-align: right; }

  .contact { text-align: center; font-size: 10.5px; line-height: 1.55; color: var(--ink-soft); }
  .contact .phone { font-size: 12.5px; font-weight: 600; color: var(--ink); }

  .services {
    font-family: "Trocchi", serif; font-size: 22px; line-height: 1.08;
    text-align: center; color: var(--ink);
  }
  .rule { height: 1px; background: var(--rule); margin: 0 14px; }
  .offer { text-align: center; font-family: "Trocchi", serif; font-size: 22px; line-height: 1.1; }
  .offer small { display: block; font-family: "Montserrat", sans-serif; font-size: 10px; color: var(--ink-soft); margin-top: 2px; }
  .big-phone { text-align: center; font-family: "Trocchi", serif; font-size: 15px; line-height: 1.25; }
  .cover-contact { text-align: center; font-size: 9.5px; line-height: 1.4; color: var(--ink-soft); }

  ul.points { list-style: disc; padding-left: 13px; }
  ul.points li { margin-bottom: 1px; }
  .sub-label { margin-top: 5px; }
  .call { font-size: 10.5px; color: var(--ink-soft); }
  .call strong { font-family: "Trocchi", serif; font-weight: 400; font-size: 16px; color: var(--ink); }

  .pricing { width: 100%; border-collapse: collapse; font-size: 9px; }
  .pricing th { background: var(--ink); color: var(--paper); font-weight: 500; padding: 3px 3px; text-align: center; }
  .pricing td { border: 1px solid var(--rule); padding: 2px 4px; text-align: center; color: var(--ink-soft); }
  .pricing td:first-child { text-align: left; }
</style>
</head>
<body>

<!-- Outside of the trifold -->
<section class="sheet sheet--outside" aria-label="Brochure outside">
  <div class="fold fold--a"></div>
  <div class="fold fold--b"></div>
  <svg class="swoosh" viewBox="0 0 1000 570" aria-hidden="true">
    <path d="M0 248 Q200 330 560 312 Q200 336 0 272 Z" fill="var(--ink)"/>
    <path d="M666 196 Q830 214 1000 248 L1000 266 Q830 232 666 206 Z" fill="var(--ink)"/>
    <circle cx="833" cy="222" r="24" fill="var(--ink)"/>
  </svg>

  <div class="panel panel--1">
    <div class="block" style="top:42px">
      <h2 class="heading center">Our Mission:</h2>
      <span class="flourish"></span>
      <p class="body-text justify">is to care for your pet in the best way possible when you are away. We provide a unique social experience for dogs and cats and create a new standard for pet care. We have set out to create a facility that exemplifies what we ourselves would want for our own best friends. Your pet will have a fun, safe place to play during the day and a secure night time environment when staying with us. Our staff will go to any lengths to make our guests stay a true delight.</p>
    </div>
    <div class="block wordmark" style="top:370px">
      <div class="wordmark__dot"></div>
      <div class="wordmark__name">Hollowmere Pet<br>Lodge &amp; Spa</div>
    </div>
  </div>

  <div class="panel panel--2">
    <div class="block" style="top:70px">
      <h2 class="heading center">Hours of Operation</h2>
      <span class="flourish"></span>
      <table class="hours">
        <tr><td>Monday</td><td>7:30am - 6:30pm</td></tr>
        <tr><td>Tuesday</td><td>7:30am - 6:30pm</td></tr>
        <tr><td>Wednesday</td><td>7:30am - 6:30pm</td></tr>
        <tr><td>Thursday</td><td>7:30am - 6:30pm</td></tr>
        <tr><td>Friday</td><td>7:30am - 6:30pm</td></tr>
        <tr><td>Saturday</td><td>8:30am - 6:30pm</td></tr>
        <tr><td>Sunday</td><td>10:30am - 6:30pm</td></tr>
      </table>
    </div>
    <div class="block wordmark" style="top:350px">
      <div class="wordmark__dot"></div>
      <div class="wordmark__name">Hollowmere Pet<br>Lodge &amp; Spa</div>
    </div>
    <div class="block contact" style="top:445px">
      72 Alder Mill Road<br>
      Hollowmere, OH 43000<br>
      info@hollowmerepetlodge.com<br>
      <span class="phone">555-014-2286</span><br>
      <span class="phone">Fax- 555-014-2285</span>
    </div>
  </div>

  <div class="panel panel--3">
    <div class="block wordmark wordmark--large" style="top:62px">
      <div class="wordmark__dot"></div>
      <div class="wordmark__name">Hollowmere Pet<br>Lodge &amp; Spa</div>
    </div>
    <div class="block" style="top:264px">
      <p class="services">Grooming<br>Boarding<br>Daycare<br>Pet Boutique</p>
    </div>
    <div class="block" style="top:368px"><div class="rule"></div></div>
    <div class="block" style="top:380px">
      <p class="offer">$10.00 OFF<small>First Time Grooming Visit</small></p>
    </div>
    <div class="block" style="top:432px"><div class="rule"></div></div>
    <div class="block" style="top:442px">
      <p class="big-phone">555-014-2286<br>Fax-555-014-2285</p>
    </div>
    <div class="block" style="top:486px"><div class="rule"></div></div>
    <div class="block" style="top:496px">
      <p class="cover-contact">72 Alder Mill Road<br>Hollowmere, OH 43000<br>info@hollowmerepetlodge.com</p>
    </div>
  </div>
</section>

<!-- Inside of the trifold -->
<section class="sheet sheet--inside" aria-label="Brochure inside">
  <div class="fold fold--a"></div>
  <div class="fold fold--b"></div>
  <svg class="swoosh" viewBox="0 0 1000 570" aria-hidden="true">
    <path d="M0 256 Q170 240 333 222 L333 234 Q170 252 0 272 Z" fill="var(--ink)"/>
    <ellipse cx="228" cy="240" rx="28" ry="23" fill="var(--ink)"/>
    <ellipse cx="286" cy="230" rx="28" ry="23" fill="var(--ink)"/>
    <path d="M880 56 Q940 44 1000 36 L1000 46 Q940 54 880 64 Z" fill="var(--ink)"/>
    <circle cx="960" cy="42" r="22" fill="var(--ink)"/>
    <path d="M890 340 Q945 330 1000 324 L1000 334 Q945 340 890 348 Z" fill="var(--ink)"/>
    <circle cx="960" cy="330" r="22" fill="var(--ink)"/>
  </svg>

  <div class="panel panel--1">
    <div class="block" style="top:22px">
      <p class="body-text justify">Hollowmere Pet Lodge &amp; Spa is a high-quality, full-service pet facility with passionate and trained animal loving staff members who will treat your pets like family. We provide our canine and feline guests with the expert care and attention that they deserve and require. We are passionate about animals and understand that they all have their own individual personalities. We take the time to get to know your best friend and give them the individual care they need. Our services include dog daycare, dog and cat boarding, dog and cat grooming, and a pet boutique providing a carefully curated selection of unique pet products.</p>
      <p class="call" style="margin-top:8px">Call Us Today!<br><strong>555-014-2286</strong></p>
    </div>
    <div class="block" style="top:284px">
      <h2 class="heading">Grooming</h2>
      <p class="body-text justify" style="margin-top:4px">At Hollowmere Pet Lodge &amp; Spa our experienced grooming staff will take the time to make your pet look fabulous using state-of-the-art grooming equipment and techniques. Our professional master groomers are friendly pet lovers who take great pride in their work. Whether you need professional grooming, premium bathing services, or breed standard cuts, our staff will ensure your pet walks away from our spa looking his or her best! Grooming and styling are individual spa services and pricing will vary depending upon the breed, size, style, condition and temperament of the pet. Our master groomers are eager to provide a thorough consultation which is free of charge upon arrival. At this time please express any personal requests, concerns, or any pricing questions to your master groomer.</p>
    </div>
  </div>

  <div class="panel panel--2">
    <div class="block" style="top:24px">
      <h2 class="heading">Daycare</h2>
      <p class="body-text justify" style="margin-top:4px">Our dog daycare play rooms are supervised by our trained staff members so that your pet can have a safe place to socialize, exercise, and expend energy. We have dedicated play rooms to accommodate different sized guests with different temperaments. We provide your pet with a safe, clean and fun environment that will remind your best friend of being at home.</p>
    </div>
    <div class="block" style="top:160px">
      <h2 class="heading">Pricing and Requirements for Daycare and Boarding</h2>
      <p class="body-text justify" style="margin-top:5px">We require all guests to complete an evaluation prior to entering our dog daycare program. This evaluation will determine whether your pet is safe to play with other dogs and members of our staff.</p>
      <p class="body-text sub-label">For all canine guests:</p>
      <ul class="points body-text">
        <li>Proof of current DHPPv/DHPP2v (yearly), Rabies, and Bordetella (yearly).</li>
        <li>All vaccinations must be current prior to dog daycare or boarding.</li>
      </ul>
      <p class="body-text sub-label">For all feline guests:</p>
      <ul class="points body-text">
        <li>Proof of current Rabies, and FVRCP vaccinations.</li>
        <li>All vaccinations must be current prior to boarding.</li>
      </ul>
    </div>
    <div class="block" style="top:430px">
      <table class="pricing">
        <tr><th>Daycare Pricing</th><th>Single Pet</th><th>Add'l Pet</th><th>3rd/4th Pet</th></tr>
        <tr><td>4 Hours</td><td>$12</td><td>$9</td><td>$6</td></tr>
        <tr><td>6 Hours</td><td>$17</td><td>$13</td><td>$10</td></tr>
        <tr><td>Full Day</td><td>$22</td><td>$16</td><td>$12</td></tr>
        <tr><td>Dog Boarding</td><td>$32</td><td>$26</td><td>$21</td></tr>
        <tr><td>Cat Boarding</td><td>$15</td><td>$13</td><td></td></tr>
      </table>
    </div>
  </div>

  <div class="panel panel--3">
    <div class="block" style="top:24px; right:80px">
      <h2 class="heading">While Your Dog<br>Is With Us....</h2>
    </div>
    <div class="block" style="top:68px">
      <ul class="points body-text body-text--tight">
        <li>They will stay in our brand new state-of-the-art boarding suites</li>
        <li>Suites are supplied with elevated beds, blankets and toys</li>
        <li>Off leash dog daycare within a supervised and safe environment</li>
        <li>Dog daycare rooms include a flat screen television, elevated cots, and a state-of-the-art gym to give each dog the feeling of home</li>
        <li>Building equipped throughout with central heat and air conditioning</li>
        <li>A secure fenced-in facility for our guests</li>
        <li>Wellness checks provided with continuous monitoring of your pet throughout their visit</li>
        <li>We offer 24/7 camera monitoring to ensure a safe, relaxing and comfortable experience for your pets and added security</li>
        <li>Our pet boutique will offer retail merchandise such as toys, treats, pet food, beds, pet clothing apparel, collars, leashes and much more...</li>
      </ul>
    </div>
    <div class="block" style="top:348px; right:80px">
      <h2 class="heading">While Your Cat<br>Is With Us....</h2>
    </div>
    <div class="block" style="top:390px">
      <ul class="points body-text body-text--tight">
        <li>Your cat will thoroughly enjoy their privacy in our luxurious boarding room away from the canine guests</li>
        <li>They will stay in our brand new state-of-the-art kitty condo suites</li>
        <li>Comfortable bedding for each guest will be provided along with toys as well as all other necessary amenities and essentials for your cat(s) stay with us</li>
        <li>Each guest will have individual play times outside of their suites with our staff members.</li>
        <li>Toys and climbing structures will be accessible to ensure a happy visit</li>
      </ul>
    </div>
    <div class="block" style="top:538px">
      <p class="call">Call Us Today! <strong>555-014-2286</strong></p>
    </div>
  </div>
</section>

</body>
</html>
```